Kestrel Photography Business Card

I need a business card designed for a photography business based in Perth, Western Australia called Kestrel Photography.

We specialise in wedding, event photography and portrait photography.

The business card must borrow the style of the attached logo.

The hex codes for the colours in the logo are:
#ED1D85 - Pink
#89C23E - Green
#37282F - Black

The name on the card will be:
Name: Toviran
Phone: 0417395268
Website: www.kestrelphotography.com.au
Facebook: kestrelphotography

I am open and happy to accept creative concepts.

I’d like some space at the back for writing notes and appointment details.

```html
<!DOCTYPE html>
<html lang="en">
<head>
<meta charset="utf-8">
<title>Kestrel Photography Business Card</title>
<link rel="stylesheet" href="https://fonts.googleapis.com/css2?family=Questrial&family=Montserrat:wght@700&display=swap">
<style>
  :root {
    --pink: #ED1D85;
    --green: #89C23E;
    --lime: #a4c93d;
    --ink: #37282F;
    --plum: #4a3a42;
    --cream: #f2eef0;
    --stage: #e6e3e4;
  }
  * { margin: 0; padding: 0; box-sizing: border-box; }
  html, body { width: 1200px; height: 900px; overflow: hidden; }
  body {
    background: var(--stage);
    display: flex;
    align-items: center;
    justify-content: center;
    gap: 48px;
    font-family: "Questrial", sans-serif;
  }
  .card {
    width: 540px;
    height: 310px;
    border-radius: 16px;
    position: relative;
    box-shadow: 0 10px 30px rgba(55, 40, 47, 0.25);
  }
  .card--front {
    background: var(--plum);
    display: flex;
    flex-direction: column;
    align-items: center;
    justify-content: center;
    gap: 34px;
  }
  .brand-dot {
    width: 78px;
    height: 78px;
    border-radius: 50%;
    background: var(--pink);
  }
  .brand-name {
    color: var(--cream);
    font-size: 22px;
    letter-spacing: 0.42em;
    text-transform: uppercase;
    padding-left: 0.42em;
  }
  .card--back {
    background: var(--lime);
    color: var(--ink);
    padding: 40px 0 0 0;
    display: flex;
    flex-direction: column;
    align-items: center;
  }
  .back-dot {
    width: 44px;
    height: 44px;
    border-radius: 50%;
    background: var(--pink);
    margin-bottom: 18px;
  }
  .back-name {
    font-size: 15px;
    letter-spacing: 0.42em;
    text-transform: uppercase;
    padding-left: 0.42em;
    margin-bottom: 26px;
  }
  .contact-list {
    list-style: none;
    font-size: 14px;
    letter-spacing: 0.16em;
    text-transform: uppercase;
    line-height: 1.7;
  }
  .contact-item { display: flex; align-items: center; gap: 8px; }
  .contact-icon { width: 13px; height: 13px; flex: none; }
  .contact-phone { font-size: 16px; }
  .contact-person {
    margin-top: 14px;
    font-family: "Montserrat", sans-serif;
    font-weight: 700;
    font-size: 13px;
    letter-spacing: 0.2em;
    text-transform: uppercase;
  }
</style>
</head>
<body>
  <section class="card card--front" aria-label="Card front">
    <div class="brand-dot"></div>
    <h1 class="brand-name">Kestrel Photography</h1>
  </section>

  <section class="card card--back" aria-label="Card back">
    <div class="back-dot"></div>
    <h2 class="back-name">Kestrel Photography</h2>
    <ul class="contact-list">
      <li class="contact-item contact-phone">
        <svg class="contact-icon" viewBox="0 0 16 16" aria-hidden="true">
          <path fill="var(--ink)" d="M4 1h3l1 4-2 1c1 2 2 3 4 4l1-2 4 1v3c0 1-1 2-2 2C7 14 2 9 2 3c0-1 1-2 2-2z"/>
        </svg>
        0417395268
      </li>
      <li class="contact-item">
        <span class="contact-icon"></span>
        www.kestrelphotography.com.au
      </li>
      <li class="contact-item">
        <svg class="contact-icon" viewBox="0 0 16 16" aria-hidden="true">
          <rect width="16" height="16" rx="2" fill="var(--ink)"/>
        </svg>
        kestrelphotography
      </li>
      <li class="contact-item contact-person">
        <span class="contact-icon"></span>
        Toviran
      </li>
    </ul>
  </section>
</body>
</html>
```